Bolvarin Incorporated

Bolvarin is a business that provides consulting, and manages and supplies trades persons in the construction and heavy industries sector. We build, do maintenance, install machinery, and can manage projects or jobs. Would like or prefer more clean, classic designs. Blacks/greys, but open to almost anything.

Target Market(s)

Industrial/Construction/Manufacturing

Industry/Entity Type

Construction Company

Contact Information for Business Card

Clean, business name on the front, possibly have the details on the back, but open to any ideas.

Logo Text

We currently do not have a slogan, open to ideas

Font styles to use
Serif
Sans Serif

Colors

Designer to choose colors to be used in the design.

Requirements
Should not have
• the oval is not my logo, was just an idea. please don't send 20 designs with the oval

```html
<!DOCTYPE html>
<html lang="en">
<head>
<meta charset="utf-8">
<title>Bolvarin Incorporated – Business Card</title>
<link rel="stylesheet" href="https://fonts.googleapis.com/css2?family=Arimo:wght@700&family=Lato:wght@400&display=swap">
<style>
  :root {
    --page-bg: #e9e8e6;
    --card-light: #f7f6f5;
    --card-light-edge: #ecebea;
    --band-dark: #1b1a1f;
    --ink: #151417;
    --text-light: #f2f2f2;
    --text-muted: #c9c9cc;
    --divider: #4a494e;
  }
  * { margin: 0; padding: 0; box-sizing: border-box; }
  html, body {
    width: 1200px; height: 900px; overflow: hidden;
    background: var(--page-bg);
  }
  .card {
    position: absolute; left: 100px; top: 140px;
    width: 1000px; height: 623px;
    background: var(--band-dark);
    box-shadow: 0 10px 30px rgba(0,0,0,0.18);
    overflow: hidden;
  }
  .card__top {
    position: absolute; left: 0; top: 0; width: 100%; height: 340px;
    background: linear-gradient(180deg, var(--card-light) 0%, var(--card-light-edge) 100%);
    display: flex; align-items: center; justify-content: center;
  }
  .card__rule {
    position: absolute; left: 0; top: 340px; width: 100%; height: 4px;
    background: var(--ink);
  }
  .card__gap {
    position: absolute; left: 0; top: 344px; width: 100%; height: 6px;
    background: var(--card-light-edge);
  }
  .brand-name {
    font-family: "Lato", sans-serif; font-weight: 400;
    font-size: 66px; color: var(--ink); letter-spacing: 1px;
  }
  .identity {
    position: absolute; right: 534px; top: 410px; text-align: right;
  }
  .identity__name {
    font-family: "Arimo", sans-serif; font-weight: 700;
    font-size: 34px; color: var(--text-light); line-height: 40px;
  }
  .identity__role {
    font-family: "Lato", sans-serif; font-size: 26px;
    color: var(--text-muted); line-height: 36px;
  }
  .divider {
    position: absolute; left: 505px; top: 400px; width: 1px; height: 120px;
    background: var(--divider);
  }
  .contacts {
    position: absolute; left: 528px; top: 402px; list-style: none;
  }
  .contacts li {
    display: flex; align-items: center; gap: 8px;
    font-family: "Lato", sans-serif; font-size: 28px;
    color: var(--text-muted); line-height: 37px;
  }
  .contacts svg { width: 22px; height: 22px; fill: var(--text-muted); flex: none; }
  .address {
    position: absolute; left: 0; width: 100%; top: 532px;
    text-align: center; padding-left: 80px;
    font-family: "Lato", sans-serif; font-size: 28px; color: var(--text-muted);
  }
</style>
</head>
<body>
  <div class="card">
    <div class="card__top">
      <span class="brand-name">Bolvarin Incorporated</span>
    </div>
    <div class="card__rule"></div>
    <div class="card__gap"></div>

    <div class="identity">
      <p class="identity__name">MARCUS HALLETT</p>
      <p class="identity__role">Managing Director</p>
    </div>

    <div class="divider"></div>

    <ul class="contacts">
      <li>
        <svg viewBox="0 0 24 24" aria-hidden="true"><path d="M3 8c0-2 4-4 9-4s9 2 9 4v2h-5V8H8v2H3zM6 11h12l2 9H4zM12 13a3 3 0 1 0 0 6a3 3 0 1 0 0-6z"/></svg>
        044-318 502 746
      </li>
      <li>
        <svg viewBox="0 0 24 24" aria-hidden="true"><path d="M2 5h20v14H2zM4 7v.5l8 6 8-6V7zM4 10v7h16v-7l-8 6z"/></svg>
        office@bolvarin.com
      </li>
      <li>
        <svg viewBox="0 0 24 24" aria-hidden="true"><path d="M12 2a10 10 0 1 0 0 20a10 10 0 1 0 0-20zM8 7l3 1 1 3-2 2 1 4-3-2-1-4-2-1zM15 13l3 1-1 4-3 1z"/></svg>
        www.bolvarin.com
      </li>
    </ul>

    <p class="address">418, Foundry Road, Eastvale, 45310, Keravia</p>
  </div>
</body>
</html>
```